Modern Business Card for Lanternfield 2018

Our company assumes the best about people. We are creating an online community of entrepreneurs and business leaders who struggle with marketing their business online.

This business card should POP! We recently got a new logo and are launching a new website next month, so our business cards should make a statement that feels:
-Fresh
-Smart
-Trustworthy
-Fun

Target Market(s)

small business owners, entrepreneurs

Industry/Entity Type

Digital Marketing

Contact Information for Business Card

Dimensions: 3.5" x 2"

Font styles to use
Sans Serif

Colors
f37122
ffffff

Requirements
Must have
• We need a business card with a modern, bold design. We will use one side of the card as a lead-generation offer, so text on one side will need to fit up to 140 characters. The business card should stick to our core colors (orange, black, and white).
Nice to have
• We think a vertical "portrait" design could be interesting.
Should not have
• Should not look like a traditional business card. The round icon should stand out from a distance.

```html
<!DOCTYPE html>
<html lang="en">
<head>
<meta charset="utf-8">
<title>Lanternfield Business Card</title>
<link rel="stylesheet" href="https://fonts.googleapis.com/css2?family=Lato:wght@400;700;900&display=swap">
<style>
  :root {
    --orange: #f37122;
    --white: #ffffff;
    --card-white: #f4f4f4;
    --black: #1a1a1a;
    --ink: #3a3a3a;
    --stage: #e9e6e2;
  }
  * { margin: 0; padding: 0; box-sizing: border-box; }
  html, body { width: 1200px; height: 900px; overflow: hidden; }
  body {
    background: var(--stage);
    font-family: "Lato", sans-serif;
    position: relative;
  }
  .card {
    position: absolute;
    width: 600px;
    height: 343px;
    border-radius: 4px;
    overflow: hidden;
    box-shadow: 0 10px 28px rgba(0,0,0,0.18);
  }

  /* Back side: lead-generation offer */
  .card-back {
    left: 110px; top: 100px;
    background: var(--orange);
    color: var(--white);
    text-align: center;
  }
  .back-brand {
    position: absolute; left: 0; right: 0; top: 62px;
    display: flex; align-items: center; justify-content: center; gap: 14px;
  }
  .back-brand .dot {
    width: 52px; height: 52px; border-radius: 50%; background: var(--white);
  }
  .back-brand .name {
    font-weight: 900; font-size: 40px; letter-spacing: 1px; text-transform: uppercase;
  }
  .back-rule {
    position: absolute; left: 90px; right: 90px; top: 168px;
    height: 1px; background: rgba(255,255,255,0.45);
  }
  .offer {
    position: absolute; left: 60px; right: 60px; top: 186px;
    font-size: 19px; line-height: 1.3; font-weight: 400;
  }

  /* Front side: contact details */
  .card-front {
    left: 490px; top: 457px;
    background: var(--card-white);
  }
  .card-front .wave { position: absolute; inset: 0; width: 100%; height: 100%; }
  .person { position: absolute; left: 40px; top: 30px; }
  .person-name {
    color: var(--orange); font-weight: 700; font-size: 25px; letter-spacing: 0.5px;
  }
  .person-role { color: var(--ink); font-size: 18px; margin-top: 2px; }
  .contact { position: absolute; left: 40px; top: 120px; list-style: none; }
  .contact li {
    display: flex; align-items: center; gap: 9px;
    color: var(--ink); font-size: 18px; line-height: 1.35;
  }
  .contact svg { width: 15px; height: 15px; flex: none; }
  .slogan {
    position: absolute; left: 40px; top: 180px;
    color: var(--orange); font-size: 20px; line-height: 1.3;
    text-transform: uppercase; letter-spacing: 0.3px;
  }
  .front-brand {
    position: absolute; right: 30px; top: 40px; text-align: center;
  }
  .front-brand .dot {
    width: 38px; height: 38px; border-radius: 50%;
    background: var(--orange); margin: 0 auto 6px;
  }
  .front-brand .name {
    color: var(--orange); font-weight: 900; font-size: 34px; letter-spacing: 0.5px;
    text-transform: uppercase;
  }
  .front-brand .tagline {
    color: var(--orange); font-weight: 700; font-size: 12px; letter-spacing: 0.8px;
    text-transform: uppercase; margin-top: 2px;
  }
</style>
</head>
<body>

  <section class="card card-back">
    <div class="back-brand">
      <span class="dot"></span>
      <span class="name">Lanternfield</span>
    </div>
    <div class="back-rule"></div>
    <p class="offer">Get your free Lanternfield Starter Package and<br>our marketing guide today at<br>lanternfieldnow.com/start</p>
  </section>

  <section class="card card-front">
    <svg class="wave" viewBox="0 0 600 343" preserveAspectRatio="none" aria-hidden="true">
      <path d="M0,292 C220,305 360,285 450,210 C500,172 545,165 600,166 L600,343 L0,343 Z" fill="var(--black)"/>
      <path d="M0,322 C220,330 370,300 470,222 C520,185 560,176 600,176 L600,343 L0,343 Z" fill="var(--orange)"/>
    </svg>

    <div class="person">
      <h1 class="person-name">DANA WHITLOCK</h1>
      <p class="person-role">Story Marketing Coach</p>
    </div>

    <ul class="contact">
      <li>
        <svg viewBox="0 0 16 16"><rect x="1" y="3" width="14" height="10" fill="var(--orange)"/><path d="M1,3 L8,9 L15,3" stroke="var(--card-white)" stroke-width="1.4" fill="none"/></svg>
        dana@lanternfieldnow.com
      </li>
      <li>
        <svg viewBox="0 0 16 16"><circle cx="8" cy="8" r="7" fill="var(--orange)"/><path d="M1,8 H15 M8,1 C4,5 4,11 8,15 M8,1 C12,5 12,11 8,15" stroke="var(--card-white)" stroke-width="1" fill="none"/></svg>
        www.lanternfieldnow.com
      </li>
    </ul>

    <p class="slogan">Reach more people<br>Make more money<br>Create more impact.</p>

    <div class="front-brand">
      <div class="dot"></div>
      <div class="name">Lanternfield</div>
      <div class="tagline">Tell stories that inspire action</div>
    </div>
  </section>

</body>
</html>
```